Wine Label for a wine from Tuscany, Italy

We need a wine label for a white and red wine, can be the same label or can be somewhat differentiated with any variation you feel would be good.. These two wines come from Tuscany, Italy. Wine labels from Tuscany Italy tend to be traditional. We are open to traditional looking labels but also more modern, eye catching too. We want to convey a sense of elegance, importance, great wine. I am attaching some examples of labels we like from Tuscany, also a label that was designed for us recently by one of you, which we LOVE. No wine glasses, wine bottles or grapes featured on the label please. We tend to like the white background. No blue please.

Target Market(s)

More women than men purchase wine, but it needs to appeal to both sexes.

Requirements
Must have
• Wine Name: Corte L' or Corte l'
• Type/Varletal: Rosso Toscano (White is Vermentino)
• Vintage (year): 2018
• That is all the text we want on the label, thanks
Nice to have
• Clean, something that makes someone want to grab this wine bottle off the shelf!
Should not have
• Images of Wine glass, wine bottles, grapes
• Do not use the color blue please.

```html
<!DOCTYPE html>
<html lang="it">
<head>
<meta charset="utf-8">
<title>Corte L' — Rosso Toscano 2018</title>
<link rel="stylesheet" href="https://fonts.googleapis.com/css2?family=Noto+Serif:wght@400&family=Oswald:wght@300&display=swap">
<style>
  :root {
    --backdrop: #cfc6c2;
    --paper: #efe3dc;
    --copper: #b8733e;
    --copper-light: #d69a62;
    --ink: #1c1714;
    --muted-ink: #5a4a42;
  }
  * { margin: 0; padding: 0; box-sizing: border-box; }
  html, body {
    width: 1200px;
    height: 1200px;
    overflow: hidden;
    background: var(--backdrop);
  }
  .canvas {
    position: relative;
    width: 1200px;
    height: 1200px;
    display: flex;
    align-items: center;
    justify-content: center;
  }
  .wine-label {
    position: relative;
    width: 900px;
    height: 960px;
    background: var(--paper);
    box-shadow: 0 6px 18px rgba(60, 40, 30, 0.18);
  }
  .label-frame {
    position: absolute;
    inset: 0;
    width: 100%;
    height: 100%;
  }
  .brand-mark {
    position: absolute;
    top: 230px;
    left: 0;
    right: 0;
    text-align: center;
    font-family: "Noto Serif", Georgia, serif;
    font-weight: 400;
    font-size: 170px;
    line-height: 1;
    color: var(--copper);
  }
  .wine-name {
    position: absolute;
    top: 660px;
    left: 0;
    right: 0;
    text-align: center;
    font-family: "Noto Serif", Georgia, serif;
    font-weight: 400;
    font-size: 50px;
    color: var(--ink);
  }
  .vintage {
    position: absolute;
    top: 790px;
    left: 0;
    right: 0;
    text-align: center;
    font-family: "Oswald", "Arial Narrow", sans-serif;
    font-weight: 300;
    font-size: 20px;
    color: var(--muted-ink);
  }
  .varietal {
    position: absolute;
    top: 830px;
    left: 0;
    right: 0;
    text-align: center;
    font-family: "Noto Serif", Georgia, serif;
    font-size: 24px;
    letter-spacing: 0.14em;
    color: var(--muted-ink);
  }
</style>
</head>
<body>
  <main class="canvas">
    <section class="wine-label">
      <svg class="label-frame" viewBox="0 0 900 960" aria-hidden="true">
        <defs>
          <linearGradient id="copper-line" x1="0" y1="0" x2="1" y2="1">
            <stop offset="0" stop-color="var(--copper-light)"/>
            <stop offset="0.5" stop-color="var(--copper)"/>
            <stop offset="1" stop-color="var(--copper-light)"/>
          </linearGradient>
        </defs>
        <polygon points="90,30 810,30 870,90 870,870 810,930 90,930 30,870 30,90"
                 fill="none" stroke="url(#copper-line)" stroke-width="4"/>
      </svg>
      <div class="brand-mark">Corte L'</div>
      <h1 class="wine-name">Corte L' or Corte l</h1>
      <p class="vintage">2018</p>
      <p class="varietal">ROSSO TOSCANO</p>
    </section>
  </main>
</body>
</html>
```